Letterhead and Envelope Design for Investment Company

We need a letterhead and envelope design.
We are a family owned investment company doing direct investments into other family owned businesses.
I have attached all our current marketing material including our logo for reference.

Our under construction website can be found here:
https://owen-darby-qk7m.sitebrella.example/
password: Marrowdale

Target Market(s)

Bankers, business owners, financial partners

Industry/Entity Type

Investment

Colors

Designer to choose colors to be used in the design.

Requirements
Must have
• Logo, and company information

```html
<!DOCTYPE html>
<html lang="en">
<head>
<meta charset="utf-8">
<title>Marrowdale Holdings, Inc. — Letterhead</title>
<link href="https://fonts.googleapis.com/css2?family=Quicksand:wght@500;600&display=swap" rel="stylesheet">
<style>
  :root {
    --paper: #ffffff;
    --ink: #1e1e1e;
    --orange: #c6672a;
    --gold: #e8b52a;
    --muted: #a3a3a3;
    --faint: #ebebeb;
  }
  html, body {
    margin: 0;
    padding: 0;
    overflow: hidden;
    background: var(--paper);
  }
  .letterhead {
    position: relative;
    width: 927px;
    height: 1200px;
    background: var(--paper);
    overflow: hidden;
    font-family: "Quicksand", sans-serif;
  }
  .brand {
    position: absolute;
    left: 66px;
    top: 104px;
    display: flex;
    align-items: center;
    gap: 10px;
  }
  .brand-dot {
    width: 14px;
    height: 14px;
    border-radius: 50%;
    background: var(--gold);
  }
  .brand-name {
    font-size: 22px;
    font-weight: 600;
    color: var(--ink);
    letter-spacing: 0.5px;
  }
  .contact {
    position: absolute;
    left: 576px;
    top: 52px;
    font-size: 12.6px;
    font-weight: 500;
    color: var(--muted);
  }
  .contact-company {
    color: var(--orange);
    font-size: 13.6px;
    margin: 0 0 6px;
  }
  .contact-list {
    list-style: none;
    margin: 0;
    padding: 0;
  }
  .contact-list li {
    display: flex;
    align-items: center;
    gap: 5px;
    height: 21.6px;
  }
  .contact-list svg {
    width: 16px;
    height: 16px;
    flex: none;
  }
  .backdrop-name {
    position: absolute;
    left: 0;
    width: 927px;
    top: 610px;
    text-align: center;
    font-size: 62px;
    font-weight: 600;
    color: var(--faint);
    letter-spacing: 2px;
  }
  .footer-band {
    position: absolute;
    left: 0;
    bottom: 0;
    width: 927px;
    height: 56px;
  }
</style>
</head>
<body>
<div class="letterhead">
  <div class="brand">
    <span class="brand-dot"></span>
    <span class="brand-name">Marrowdale Holdings</span>
  </div>

  <div class="contact">
    <p class="contact-company">Marrowdale Holdings, Inc.</p>
    <ul class="contact-list">
      <li>
        <svg viewBox="0 0 16 16" fill="none" stroke="#c6672a" stroke-width="1.3">
          <path d="M8 1.5a4 4 0 0 0-4 4c0 3 4 6.5 4 6.5s4-3.5 4-6.5a4 4 0 0 0-4-4z" fill="#c6672a"/>
          <circle cx="8" cy="5.5" r="1.4" fill="#fff" stroke="none"/>
          <path d="M2 14.5h12l-2-3H4z"/>
        </svg>
        418 Larch Ave. NE; Suite 210, Fenwick Falls, IA 50999
      </li>
      <li>
        <svg viewBox="0 0 16 16" fill="none" stroke="#c6672a" stroke-width="1.2">
          <circle cx="8" cy="8" r="6.8"/>
          <path d="M5.4 4.2l1.3-.3.9 2-.9.8c.4 1 1.2 1.8 2.2 2.2l.8-.9 2 .9-.3 1.3c-3.4.3-6.3-2.6-6-6z" fill="#c6672a"/>
        </svg>
        555-014-0426,
      </li>
      <li>
        <svg viewBox="0 0 16 16" fill="none" stroke="#c6672a" stroke-width="1.1">
          <circle cx="8" cy="8" r="6.8"/>
          <ellipse cx="8" cy="8" rx="3" ry="6.8"/>
          <path d="M1.2 8h13.6M2.2 4.6h11.6M2.2 11.4h11.6"/>
        </svg>
        www.marrowdaleholdings.example,
      </li>
      <li>
        <svg viewBox="0 0 16 16" fill="none" stroke="#c6672a" stroke-width="1.1">
          <circle cx="8" cy="8" r="6.8"/>
          <rect x="4.2" y="5.4" width="7.6" height="5.2"/>
          <path d="M4.2 5.4L8 8.4l3.8-3M4.2 10.6l2.6-2.4M11.8 10.6L9.2 8.2"/>
        </svg>
        inquiries@marrowdaleholdings.example
      </li>
    </ul>
  </div>

  <div class="backdrop-name" aria-hidden="true">Marrowdale Holdings</div>

  <svg class="footer-band" viewBox="0 0 927 56" preserveAspectRatio="none" aria-hidden="true">
    <polygon points="0,0 72,0 48,56 0,56" fill="var(--gold)"/>
    <polygon points="82,0 927,0 927,56 58,56" fill="var(--orange)"/>
  </svg>
</div>
</body>
</html>
```